Life Coach for Lawyers Business Card Design

Elegant, original, business card design for life coaching service for associate attorneys who work in big law and struggle with stress, overwhelm, and time management. Double sided design.

Target Market(s)

Women associate attorneys who work in big law and struggle with stress, overwhelm, and time management.

Industry/Entity Type

Life Coaching

Contact Information for Business Card

Marissa Pendrell
Life Coach
518.677.3941
calmbriefcounsel.net
marissa@calmbriefcounsel.net
@calmbriefcounsel (Instagram)

Font styles to use
Other font styles liked:
• Silver South font duo. See uploaded files.

Requirements
Must have
• Icons for phone, website, email, and Instagram instead of words. Specific colors used in my logo (171B2B, 421121, FFFFFF)
Nice to have
• Foil. Embossed. Feminine design.
Should not have
• Any colors other than those used in logo. See uploaded files.

```html
<!DOCTYPE html>
<html lang="en">
<head>
<meta charset="utf-8">
<title>Calm Brief Counsel – Business Card</title>
<link rel="stylesheet" href="https://fonts.googleapis.com/css2?family=Cormorant+Garamond:wght@500;600&display=swap">
<style>
  :root {
    --navy: #171B2B;
    --wine: #421121;
    --white: #FFFFFF;
    --backdrop: #E6E6E9;
    --rule: #6b6b72;
    --ink: #2a2a2a;
  }
  * { margin: 0; padding: 0; box-sizing: border-box; }
  html, body { width: 1200px; height: 800px; overflow: hidden; }
  body {
    background: var(--backdrop);
    font-family: "Cormorant Garamond", Georgia, serif;
    font-variant-numeric: lining-nums;
    position: relative;
  }
  .card {
    position: absolute;
    top: 245px;
    width: 540px;
    height: 309px;
    box-shadow: 0 6px 18px rgba(0,0,0,0.18);
  }
  .card--front { left: 40px; background: var(--navy); }
  .card--back { left: 620px; background: var(--white); overflow: hidden; }

  .brand {
    font-weight: 600;
    letter-spacing: 0.04em;
    line-height: 1;
    white-space: nowrap;
  }
  .card--front .brand {
    position: absolute;
    left: 0; right: 0; top: 50%;
    transform: translateY(-50%);
    text-align: center;
    color: var(--white);
    font-size: 44px;
  }

  .side-band {
    position: absolute;
    left: 0; top: 0; bottom: 0;
    width: 78px;
    background: var(--wine);
  }
  .side-rule {
    position: absolute;
    left: 84px; top: 0; bottom: 0;
    width: 1px;
    background: var(--rule);
  }
  .card--back .brand {
    position: absolute;
    left: 106px; top: 62px;
    color: var(--wine);
    font-size: 30px;
  }
  .top-rule {
    position: absolute;
    left: 378px; right: 36px; top: 58px;
    height: 1px;
    background: var(--rule);
  }
  .social-mark {
    position: absolute;
    right: 30px; top: 72px;
    width: 16px; height: 16px;
    border-radius: 3px;
    background: var(--wine);
  }
  .person {
    position: absolute;
    left: 108px; top: 150px;
    color: var(--wine);
  }
  .person__name {
    font-size: 19px;
    font-weight: 600;
    font-variant: small-caps;
    letter-spacing: 0.05em;
  }
  .person__title {
    font-size: 14px;
    color: var(--ink);
    margin-top: -2px;
  }
  .contacts {
    list-style: none;
    margin-top: 12px;
  }
  .contacts li {
    display: flex;
    align-items: center;
    gap: 8px;
    font-size: 14px;
    font-weight: 500;
    color: var(--ink);
    margin-bottom: 5px;
  }
  .contacts .icon {
    width: 16px; height: 16px;
    border-radius: 3px;
    background: var(--wine);
    display: flex;
    align-items: center;
    justify-content: center;
    flex-shrink: 0;
  }
  .contacts svg { width: 10px; height: 10px; }
</style>
</head>
<body>
  <section class="card card--front" aria-label="Card front">
    <div class="brand">Calm Brief Counsel</div>
  </section>

  <section class="card card--back" aria-label="Card back">
    <div class="side-band"></div>
    <div class="side-rule"></div>
    <div class="brand">Calm Brief Counsel</div>
    <div class="top-rule"></div>
    <div class="social-mark" role="img" aria-label="Social profile @calmbriefcounsel"></div>

    <div class="person">
      <div class="person__name">Marissa Pendrell</div>
      <div class="person__title">Life Coach</div>
      <ul class="contacts">
        <li>
          <span class="icon">
            <svg viewBox="0 0 10 10" aria-hidden="true"><path d="M2 1 L3.6 1 L4.2 3 L3.2 3.8 Q4 5.8 6.2 6.8 L7 5.8 L9 6.4 L9 8 Q8.6 9 7.6 9 Q1 8.4 1 2.4 Q1 1 2 1 Z" fill="#FFFFFF"/></svg>
          </span>
          518.677.3941
        </li>
        <li>
          <span class="icon">
            <svg viewBox="0 0 10 10" aria-hidden="true"><rect x="1" y="2.2" width="8" height="5.6" fill="none" stroke="#FFFFFF" stroke-width="0.9"/><path d="M1 2.4 L5 5.4 L9 2.4" fill="none" stroke="#FFFFFF" stroke-width="0.9"/></svg>
          </span>
          marissa@calmbriefcounsel.net
        </li>
        <li>
          <span class="icon">
            <svg viewBox="0 0 10 10" aria-hidden="true"><circle cx="5" cy="5" r="3.8" fill="none" stroke="#FFFFFF" stroke-width="0.8"/><ellipse cx="5" cy="5" rx="1.6" ry="3.8" fill="none" stroke="#FFFFFF" stroke-width="0.7"/><line x1="1.2" y1="5" x2="8.8" y2="5" stroke="#FFFFFF" stroke-width="0.7"/></svg>
          </span>
          calmbriefcounsel.net
        </li>
      </ul>
    </div>
  </section>
</body>
</html>
```